Business Card Design for Tarlo Cosmetics

hair extension supplier and mobile technican
make up and make up artistry
cosmetic eye contacts
eye lashes
general facial and hair products

```html
<!DOCTYPE html>
<html lang="en">
<head>
<meta charset="utf-8">
<title>Tarlo Cosmetics — Business Card</title>
<link href="https://fonts.googleapis.com/css2?family=Josefin+Sans:wght@300;400&family=Pinyon+Script&family=Open+Sans:wght@400&display=swap" rel="stylesheet">
<style>
  :root{
    --page:#f2f5f8;
    --ink:#141414;
    --paper:#ffffff;
    --white:#ffffff;
    --brand-dark:#262626;
    --skin-light:#efe4e0;
  }
  *{margin:0;padding:0;box-sizing:border-box}
  html,body{width:1200px;height:900px;overflow:hidden;background:var(--page)}
  .canvas{position:relative;width:1200px;height:900px}

  /* Front of card */
  .card-front{position:absolute;left:50px;top:250px;width:660px;height:400px;background:var(--paper);overflow:hidden;box-shadow:0 6px 20px rgba(0,0,0,.18)}
  .card-front .swoosh{position:absolute;inset:0}
  .photo-area{position:absolute;left:0;top:0;width:360px;height:400px;
    background:linear-gradient(90deg, var(--skin-light) 0%, var(--skin-light) 45%, rgba(255,255,255,0) 100%)}
  .holder-name{position:absolute;right:30px;top:22px;font-family:"Pinyon Script",cursive;font-size:30px;color:var(--ink)}
  .brand{position:absolute;left:270px;top:110px;color:var(--brand-dark);font-family:"Josefin Sans",sans-serif;font-weight:400;text-align:left}
  .brand .word{display:block;font-size:64px;letter-spacing:16px;line-height:1}
  .brand .sub{display:block;font-size:20px;letter-spacing:9px;margin-top:4px;padding-left:20px}
  .contacts{position:absolute;left:455px;top:276px;list-style:none;font-family:"Open Sans",sans-serif;font-size:12px;color:var(--white);line-height:1.5}
  .contacts li{display:flex;align-items:flex-start;gap:9px;margin-bottom:4px}
  .contacts svg{flex:none;width:12px;height:12px;margin-top:2px}

  /* Back of card */
  .card-back{position:absolute;left:790px;top:155px;width:360px;height:590px;background:var(--ink);overflow:hidden;box-shadow:0 6px 20px rgba(0,0,0,.25)}
  .services{position:absolute;left:5px;top:5px;right:5px;display:grid;grid-template-columns:1fr 1fr;gap:3px}
  .service{position:relative;height:78px}
  .service .tile{position:absolute;inset:0}
  .service.hair .tile{background:linear-gradient(100deg,#111 30%,#5a2a1c 65%,#a3553a)}
  .service.nails .tile{background:linear-gradient(100deg,#111 35%,#3a3a3a 70%,#8a8a88)}
  .service.eyes .tile{background:linear-gradient(100deg,#2a3a2c 25%,#6f8f6a 60%,#c9b59d)}
  .service.lashes .tile{background:linear-gradient(100deg,#0c1420 30%,#3c4f66 65%,#a3a9ae)}
  .service .label{position:absolute;left:8px;top:12px;color:var(--white);font-family:"Josefin Sans",sans-serif;font-weight:400}
  .service .label b{display:block;font-weight:400;font-size:22px;letter-spacing:5px;line-height:1}
  .service .label span{display:block;font-size:10px;letter-spacing:2px;margin-top:3px}
  .about{position:absolute;left:20px;right:20px;top:250px;text-align:center;color:var(--white);font-family:"Open Sans",sans-serif;font-size:12px;letter-spacing:1.2px;line-height:2.5}
  .back-brand{position:absolute;left:0;right:0;top:465px;text-align:center;color:var(--white);font-family:"Josefin Sans",sans-serif;font-weight:400}
  .back-brand .word{display:block;font-size:64px;letter-spacing:16px;line-height:1;padding-left:16px}
  .back-brand .sub{display:block;font-size:20px;letter-spacing:9px;margin-top:4px;padding-left:9px}
</style>
</head>
<body>
<main class="canvas">

  <section class="card-front" aria-label="Business card front">
    <div class="photo-area" role="img" aria-label="Close-up beauty photograph of an eye with long lashes"></div>
    <svg class="swoosh" viewBox="0 0 660 400" aria-hidden="true">
      <path d="M0,22 C70,22 130,26 190,28 C110,40 40,70 0,120 Z" fill="#141414"/>
      <path d="M0,400 L0,345 C210,340 430,260 660,140 L660,400 Z" fill="#141414"/>
      <path d="M30,378 C250,362 460,285 660,195" fill="none" stroke="#ffffff" stroke-width="2.5"/>
      <path d="M20,332 C240,318 440,240 660,120" fill="none" stroke="#141414" stroke-width="2"/>
    </svg>
    <p class="holder-name">Mira Castellan</p>
    <p class="brand"><span class="word">TARLO</span><span class="sub">COSMETICS</span></p>
    <ul class="contacts">
      <li><svg viewBox="0 0 12 12"><path d="M6 1 L11 6 H9.5 V11 H7 V8 H5 V11 H2.5 V6 H1 Z" fill="#fff"/></svg><span>18 Calder Lane,<br>Northbridge, WA, 6003</span></li>
      <li><svg viewBox="0 0 12 12"><rect x="3" y="1" width="6" height="10" rx="1.2" fill="#fff"/><rect x="4" y="2.5" width="4" height="5.5" fill="#141414"/></svg><span>0400 123 987</span></li>
      <li><svg viewBox="0 0 12 12"><text x="6" y="10" font-size="12" text-anchor="middle" fill="#fff" font-family="Open Sans, sans-serif">@</text></svg><span>mira@tarlocosmetics.com.au</span></li>
      <li><svg viewBox="0 0 12 12"><circle cx="6" cy="6" r="5" fill="none" stroke="#fff" stroke-width="1.2"/><path d="M1 6 H11 M6 1 C3.5 4 3.5 8 6 11 M6 1 C8.5 4 8.5 8 6 11" fill="none" stroke="#fff" stroke-width="0.9"/></svg><span>www.tarlocosmetics.com.au</span></li>
    </ul>
  </section>

  <section class="card-back" aria-label="Business card back">
    <div class="services">
      <div class="service hair"><div class="tile" role="img" aria-label="Photograph of flowing auburn hair"></div><p class="label"><b>TARLO</b><span>HAIR</span></p></div>
      <div class="service nails"><div class="tile" role="img" aria-label="Photograph of manicured nails"></div><p class="label"><b>TARLO</b><span>NAILS</span></p></div>
      <div class="service eyes"><div class="tile" role="img" aria-label="Photograph of an eye with green make-up"></div><p class="label"><b>TARLO</b><span>EYES</span></p></div>
      <div class="service lashes"><div class="tile" role="img" aria-label="Photograph of an eye with long lashes"></div><p class="label"><b>TARLO</b><span>LASHES</span></p></div>
    </div>
    <p class="about">Tarlo Cosmetics is the company for my<br>businesses, Tarlo Hair, Tarlo Lashes,<br>Tarlo Nails &amp; Tarlo Eyes</p>
    <p class="back-brand"><span class="word">TARLO</span><span class="sub">COSMETICS</span></p>
  </section>

</main>
</body>
</html>
```